Military training company needs a Powerpoint desk template.

We need a Powerpoint deck that we can use for sales and training purposes. We are a training company for military mountaineering, so need something simple, clean and uncluttered that incorporates our logo and includes a placeholder for our tagline (under development). The colors need to complement and/or include the colors in the logo that was designed by Brightloom (attached below)

Requirements
Must have
• We need a title slide, table of content, etc. Please use the fonts and colors in the logo.

```html
<!DOCTYPE html>
<html lang="en">
<head>
<meta charset="utf-8">
<title>Altavir – Presentation Template Overview</title>
<link rel="stylesheet" href="https://fonts.googleapis.com/css2?family=Roboto:wght@400;500;700&family=Roboto+Condensed:wght@700&family=Poppins:wght@300;400;500;600;700&display=swap">
<style>
:root{
  --navy:#1c2541;
  --navy-deep:#141b30;
  --tan:#9e8662;
  --sand:#e4e0c9;
  --ink:#2a2f3d;
  --grey:#80838c;
}
*{box-sizing:border-box}
html,body{margin:0;padding:0}
body{width:1200px;height:1167px;overflow:hidden;background:linear-gradient(160deg,#97989c,#86878b);position:relative;font-family:Poppins,sans-serif}
.slide{position:absolute;width:358px;height:201px;background:#fff;overflow:hidden;box-shadow:0 2px 5px rgba(0,0,0,.35);color:var(--ink)}
.slide.dark{background:var(--navy)}
.c1{left:60px}.c2{left:429px}.c3{left:797px}
.r1{top:51px}.r2{top:266px}.r3{top:481px}.r4{top:695px}.r5{top:909px}
.abs{position:absolute}
.title{position:absolute;left:11px;top:9px;margin:0;font:500 14px/1 Roboto,sans-serif;color:var(--navy)}
.title.light{color:#fff}
.title::after{content:"";display:block;width:40px;height:2px;background:var(--tan);margin-top:5px}
.brand{position:absolute;right:10px;top:11px;font:700 6px/1 'Roboto Condensed',sans-serif;letter-spacing:1px;color:#cfc6ae}
.brand.on-dark{color:var(--tan)}
.pg{position:absolute;left:11px;bottom:4px;width:7px;height:7px;background:var(--navy);color:#fff;font:500 2.8px/7px Roboto,sans-serif;text-align:center}
.dark .pg{background:#fff;color:var(--navy)}
.base{position:absolute;left:0;right:0;bottom:5px;height:.5px;background:#c9c9c9}
.peak{position:absolute;right:0;bottom:0;width:105px;height:30px;background:linear-gradient(to top,var(--sand),rgba(228,224,201,0))}
.tiny{font-size:3.4px;line-height:1.4;color:#7a7d85;margin:0}
.tiny.light{color:#e8e8ee}
.photo{position:absolute;background:linear-gradient(135deg,#6f7a55,#8b8a6d 45%,#3e4436)}
.photo.mono{background:linear-gradient(135deg,#555,#a9a9a9 50%,#3a3a3a)}

.cover-photo{position:absolute;inset:0;background:radial-gradient(ellipse at 60% 40%,#2a3452,#141b30 75%)}
.cover-brand{position:absolute;left:0;right:0;top:78px;text-align:center;font:700 30px/1 'Roboto Condensed',sans-serif;letter-spacing:4px;color:var(--tan)}
.cover-sub{position:absolute;left:0;right:0;top:151px;text-align:center;font:500 9.5px/1 Roboto,sans-serif;color:#fff}
.cover-line{position:absolute;left:0;right:0;top:177px;height:.6px;background:var(--tan)}
.cover-url{position:absolute;left:140px;top:173px;width:78px;height:8px;border-radius:4px;background:var(--tan);color:#fff;font:400 4.5px/8px Poppins,sans-serif;text-align:center}

.agenda-item{position:absolute;width:110px}
.agenda-num{position:absolute;left:0;top:0;width:14px;height:14px;transform:rotate(45deg);background:var(--sand)}
.agenda-num span{display:block;transform:rotate(-45deg);text-align:center;font:700 9px/14px Roboto,sans-serif;color:var(--navy)}
.agenda-text{position:absolute;left:20px;top:0}
.agenda-text h3{margin:0 0 1px;font:500 5.5px/1.2 Poppins,sans-serif;color:var(--tan)}

.numlist{margin:0;padding:0;list-style:none;font:600 5.6px/12.4px Poppins,sans-serif;color:#fff}
.bullets{margin:0;padding:0;list-style:none;font:300 6px/12.4px Poppins,sans-serif;color:var(--grey)}
.bullets li::before{content:"";display:inline-block;width:2px;height:2px;background:var(--tan);margin:0 4px 1px 0}

.flow-box{position:absolute;width:60px;height:92px;border:1.6px solid var(--tan);border-radius:8px;text-align:center;padding:10px 4px 0}
.flow-icon{display:block;margin:0 auto 3px}
.flow-box h4{margin:0 0 5px;font:600 5.5px/1 Poppins,sans-serif;color:#fff}
.flow-box .tiny{font-size:3.1px;line-height:1.35}
.icon-ring{position:absolute;width:27px;height:27px;border-radius:50%;background:var(--tan);border:2.5px solid #fff;box-shadow:0 0 0 1px #ddd}
.person{position:absolute;width:24px;height:24px;border-radius:50%;background:linear-gradient(#d9d4c8,#a9a59a);border:1.5px solid #fff}
.person-name{position:absolute;width:70px;text-align:center;font:600 5.5px/1 Poppins,sans-serif;color:var(--tan)}
.phone{position:absolute;width:43px;height:91px;border:1.8px solid var(--navy);border-radius:5px;background:#fff;padding:12px 4px 0;font:400 5px/1.2 Poppins,sans-serif;color:var(--navy)}
.tab{position:absolute;width:22px;height:12px;background:var(--tan);color:#fff;font:700 8px/12px 'Roboto Condensed',sans-serif;text-align:center}
.legend-dot{display:inline-block;width:5px;height:5px;border-radius:50%;margin-right:3px;vertical-align:middle}
svg text{font-family:Poppins,sans-serif}
</style>
</head>
<body>

<section class="slide dark c1 r1">
  <div class="cover-photo" role="img" aria-label="Darkened photo of soldiers in training gear"></div>
  <div class="cover-brand">ALTAVIR</div>
  <div class="cover-sub">PRESENTATION BUSINESS MARKETING</div>
  <div class="cover-line"></div>
  <div class="cover-url">www.companywebsite.com</div>
</section>

<section class="slide c2 r1">
  <h2 class="title">Agenda</h2>
  <div class="brand">ALTAVIR</div>
  <div class="agenda-item" style="left:46px;top:72px"><div class="agenda-num"><span>1</span></div><div class="agenda-text"><h3>Lorem ipsum</h3><p class="tiny">Lorem ipsum dolor sit amet, consectetuer<br>adipiscing elit, sed diam nonummy nibh</p></div></div>
  <div class="agenda-item" style="left:46px;top:101px"><div class="agenda-num"><span>2</span></div><div class="agenda-text"><h3>Lorem ipsum</h3><p class="tiny">Lorem ipsum dolor sit amet, consectetuer<br>adipiscing elit, sed diam nonummy nibh</p></div></div>
  <div class="agenda-item" style="left:46px;top:130px"><div class="agenda-num"><span>3</span></div><div class="agenda-text"><h3>Lorem ipsum</h3><p class="tiny">Lorem ipsum dolor sit amet, consectetuer<br>adipiscing elit, sed diam nonummy nibh</p></div></div>
  <div class="agenda-item" style="left:185px;top:72px"><div class="agenda-num"><span>4</span></div><div class="agenda-text"><h3>Lorem ipsum</h3><p class="tiny">Lorem ipsum dolor sit amet, consectetuer<br>adipiscing elit, sed diam nonummy nibh</p></div></div>
  <div class="agenda-item" style="left:185px;top:101px"><div class="agenda-num"><span>5</span></div><div class="agenda-text"><h3>Lorem ipsum</h3><p class="tiny">Lorem ipsum dolor sit amet, consectetuer<br>adipiscing elit, sed diam nonummy nibh</p></div></div>
  <div class="agenda-item" style="left:185px;top:130px"><div class="agenda-num"><span>6</span></div><div class="agenda-text"><h3>Lorem ipsum</h3><p class="tiny">Lorem ipsum dolor sit amet, consectetuer<br>adipiscing elit, sed diam nonummy nibh</p></div></div>
  <div class="peak" role="img" aria-label="Mountain ridge decoration"></div>
  <div class="base"></div><div class="pg">02</div>
</section>

<section class="slide c3 r1">
  <div class="abs" style="left:248px;top:0;width:110px;height:201px;background:var(--navy)"></div>
  <div class="abs" style="left:0;top:40px;width:318px;height:144px;background:#fff"></div>
  <h2 class="title">Text Here</h2>
  <div class="brand on-dark">ALTAVIR</div>
  <div class="abs" style="left:16px;top:56px;width:172px">
    <div style="font:500 9.5px/1.25 Roboto,sans-serif;color:var(--tan)">Lorem Ipsum<br>Dolor Sit Ametkeeper.</div>
    <p class="tiny" style="margin-top:3px">Lorem ipsum dolor sit amet, consectetuer adipiscing elit, sed diam nonummy nibh euismod tincidunt ut laoreet dolore magna aliquam erat volutpat. Ut wisi enim ad minim veniam, quis nostrud exerci tation ullamcorper suscipit lobortis nisl ut aliquip ex ea commodo consequat. Duis autem vel eum iriure dolor in hendrerit in</p>
    <p class="tiny" style="margin-top:4px">Lorem ipsum dolor sit amet, consectetuer adipiscing elit, sed diam nonummy nibh euismod tincidunt ut laoreet dolore magna aliquam erat volutpat. Ut wisi enim ad minim veniam, quis nostrud exerci tation ullamcorper suscipit lobortis nisl ut aliquip ex ea commodo consequat. Duis autem vel eum iriure dolor in hendrerit in</p>
  </div>
  <div class="photo" style="left:199px;top:59px;width:114px;height:102px" role="img" aria-label="Photo of soldiers doing push-ups on an outdoor training ground"></div>
  <div class="peak" role="img" aria-label="Mountain ridge decoration" style="opacity:.9"></div>
  <div class="base"></div><div class="pg">03</div>
</section>

<section class="slide c1 r2">
  <h2 class="title">Our Company</h2>
  <div class="brand">ALTAVIR</div>
  <div class="abs" style="left:33px;top:42px;width:150px;height:121px;background:var(--navy);padding:8px 9px">
    <p class="tiny light"><b>Lorem ipsum :</b> dolor sit amet, consectetuer adipiscing elit, nonummy nibh euismod tincidunt ut laoreet dolore magna</p>
    <p class="tiny light" style="margin-top:5px"><b>Lorem ipsum :</b> dolor sit amet, consectetuer adipiscing el sed diam nonummy nibh euismod tincidunt ut laoreet dolore magna aliquam erat volutpat. Ut wisi enim ad minim.</p>
    <p class="tiny light" style="margin-top:5px"><b>Lorem ipsum :</b> dolor sit amet, consectetuer adipis cing elit, sed diam nonummy nibh euismod tinci dunt ut laoreet magna aliquam erat volutpat.</p>
    <p class="tiny light" style="margin-top:5px"><b>Lorem ipsum :</b> dolor sit amet, consectetuer adipiscing nibh euismod tincidunt ut laoreet dolore magna</p>
    <p class="tiny light" style="margin-top:5px"><b>Lorem ipsum :</b> dolor sit amet, consectetuer adipis cing elit, sed diam nonummy nibh euismod tinci dunt ut laoreet magna aliquam erat volutpat.</p>
  </div>
  <div class="abs" style="left:199px;top:47px;font:400 8.5px/1.4 Poppins,sans-serif;color:var(--navy)">WHAT'S A DOMAIN?<br>IT'S THAT NAME UP<br><b style="color:var(--tan);font-weight:600">IN THE ADDRESS BAR.</b></div>
  <ul class="bullets abs" style="left:199px;top:86px">
    <li>Fits your business or products</li>
    <li>Is easy to spell and remember</li>
    <li>Fits your business or products</li>
    <li>Is easy to spell and remember</li>
    <li>Fits your business or products</li>
    <li>Is easy to spell and remember</li>
  </ul>
  <div class="peak" role="img" aria-label="Mountain ridge decoration"></div>
  <div class="base"></div><div class="pg">04</div>
</section>

<section class="slide dark c2 r2">
  <h2 class="title light">Our Company Education</h2>
  <div class="brand on-dark">ALTAVIR</div>
  <svg class="abs" style="left:0;top:0" width="358" height="201" viewBox="0 0 358 201" aria-hidden="true">
    <path d="M126 66 L148 126 M208 66 L230 126" stroke="var(--tan)" stroke-width="1.4" fill="none"/>
    <circle cx="126" cy="66" r="2.6" fill="var(--tan)"/><circle cx="148" cy="126" r="2.6" fill="var(--tan)"/>
    <circle cx="208" cy="66" r="2.6" fill="var(--tan)"/><circle cx="230" cy="126" r="2.6" fill="var(--tan)"/>
  </svg>
  <div class="flow-box" style="left:66px;top:47px">
    <svg class="flow-icon" width="10" height="10" viewBox="0 0 10 10" aria-hidden="true"><g stroke="#fff" stroke-width=".8" fill="none"><circle cx="5" cy="4" r="3"/><path d="M3.8 7.6 h2.4 M4 9 h2"/></g></svg>
    <h4>IDEA</h4>
    <p class="tiny light">Lorem ipsum dolor sit amet, consectetuer adipiscing elit, sed diam nonummy nibh euismod tincidunt ut laoreet dolore magna aliquam erat volutpat. Ut wisi enim ad minim veniam, quis nostrud exerci tation ullamcorper suscipit lobortis nisl ut aliquip ex ea</p>
  </div>
  <div class="flow-box" style="left:148px;top:47px">
    <svg class="flow-icon" width="10" height="10" viewBox="0 0 10 10" aria-hidden="true"><g stroke="#fff" stroke-width=".8" fill="none"><rect x="1" y="2.5" width="8" height="5.5"/><path d="M1 2.5 l4 3 l4-3"/></g></svg>
    <h4>PROMOTION</h4>
    <p class="tiny light">Lorem ipsum dolor sit amet, consectetuer adipiscing elit, sed diam nonummy nibh euismod tincidunt ut laoreet dolore magna aliquam erat volutpat. Ut wisi enim ad minim veniam, quis nostrud exerci tation ullamcorper suscipit lobortis nisl ut aliquip ex ea</p>
  </div>
  <div class="flow-box" style="left:230px;top:47px">
    <svg class="flow-icon" width="10" height="10" viewBox="0 0 10 10" aria-hidden="true"><g stroke="#fff" stroke-width=".8" fill="none"><path d="M1 1 v8 h8 M2.5 7.5 l5-5 M5.5 2.5 h2 v2"/></g></svg>
    <h4>GROWTH</h4>
    <p class="tiny light">Lorem ipsum dolor sit amet, consectetuer adipiscing elit, sed diam nonummy nibh euismod tincidunt ut laoreet dolore magna aliquam erat volutpat. Ut wisi enim ad minim veniam, quis nostrud exerci tation ullamcorper suscipit lobortis nisl ut aliquip ex ea</p>
  </div>
  <p class="tiny light abs" style="left:40px;top:148px;width:278px;text-align:center;font-size:3.8px">Lorem ipsum dolor sit amet, consectetuer adipiscing elit, sed diam nonummy nibh euismod tincidunt ut laoreet dolore magna aliquam erat volutpat. Ut wisi enim ad minim veniam, quis nostrud exerci tation ullamcorper suscipit lobortis nisl ut aliquip ex ea commodo consequat. Duis autem vel eum iriure dolor in hendrerit i</p>
  <div class="peak" role="img" aria-label="Mountain ridge decoration" style="background:linear-gradient(to top,rgba(228,224,201,.9),rgba(228,224,201,0))"></div>
  <div class="pg">05</div>
</section>

<section class="slide c3 r2">
  <h2 class="title">About Us Company</h2>
  <div class="brand">ALTAVIR</div>
  <div class="abs" style="left:21px;top:42px;width:170px;height:127px;background:var(--navy);padding:7px 9px 0 11px">
    <p class="tiny light">Lorem ipsum dolor sit amet, consectetuer adipiscing elit, sed diam nonummy nibh euismod tincidunt ut laoreet dolore magna aliquam erat volutpat. Ut wisi enim ad minim veniam, quis nostrud exerci tation ullamcorper suscipit lobortis nisl ut aliquip ex ea commodo consequat. Duis autem vel eum iriure dolor in hendrerit in vulputate velit esse molestie consequat, vel illum dolore eu feugiat nulla facilisis at vero eros et accumsan et iusto odio dignissim qui blandit praesent luptatum zzril delenit augue duis dolore te feugait nulla facilisi.</p>
    <p class="tiny light" style="margin-top:4px">Lorem ipsum dolor sit amet, cons ectetuer adipiscing elit, sed diam nonummy nibh euismod tincidunt ut laoreet dolore magna aliquam erat volutpat. Ut wisi enim ad minim veniam, quis nostrud exerci tation ullamcorper suscipit lobortis nisl ut aliquip ex ea commodo consequat. Lorem ipsum dolor sit amet, consecac.</p>
  </div>
  <div class="icon-ring" style="left:178px;top:48px"></div>
  <div class="icon-ring" style="left:178px;top:92px"></div>
  <div class="icon-ring" style="left:178px;top:140px"></div>
  <div class="abs" style="left:213px;top:49px;width:135px"><div style="font:500 7px/1 Poppins,sans-serif;color:var(--tan)">Lorem ipsum</div><p class="tiny" style="margin-top:2px">ipsum dolor sit amet, cons ectetuer adipiscing elit, sed diam nonummy nibh euismod tincidunt ut laoreet</p></div>
  <div class="abs" style="left:213px;top:94px;width:135px"><div style="font:500 7px/1 Poppins,sans-serif;color:var(--tan)">Lorem ipsum</div><p class="tiny" style="margin-top:2px">ipsum dolor sit amet, cons ectetuer adipiscing elit, sed diam nonummy nibh euismod tincidunt ut laoreet dolore magna aliquam erat volutpat.</p></div>
  <div class="abs" style="left:213px;top:142px;width:135px"><div style="font:500 7px/1 Poppins,sans-serif;color:var(--tan)">Lorem ipsum</div><p class="tiny" style="margin-top:2px">ipsum dolor sit amet, cons ectetuer adipiscing elit, sed diam nonummy nibh euismod tincidunt</p></div>
  <div class="peak" role="img" aria-label="Mountain ridge decoration"></div>
  <div class="base"></div><div class="pg">06</div>
</section>

<section class="slide c1 r3">
  <div class="abs" style="left:119px;top:0;width:239px;height:201px;background:var(--navy)"></div>
  <h2 class="title">Text Here</h2>
  <div class="brand on-dark">ALTAVIR</div>
  <div class="photo" style="left:36px;top:40px;width:170px;height:126px" role="img" aria-label="Photo of soldiers doing push-ups while an instructor records results"></div>
  <ol class="numlist abs" style="left:219px;top:40px">
    <li>1. Lorem ipsum dolor sit</li>
    <li>2. Magna aliquam erat volutpat</li>
    <li>3. Ut wisi enim ad minim</li>
    <li>4. Commodo consequat.</li>
    <li>5. Lorem ipsum dolor sit</li>
    <li>6. Magna aliquam erat volutpat</li>
    <li>7. Ut wisi enim ad minim</li>
    <li>8. Dolor sit</li>
    <li>9. Ccommodo consequat.</li>
    <li>10. Magna aliquam erat volutpat</li>
  </ol>
  <div class="peak" role="img" aria-label="Mountain ridge decoration"></div>
  <div class="base"></div><div class="pg">07</div>
</section>

<section class="slide c2 r3">
  <h2 class="title">Text Here</h2>
  <div class="brand">ALTAVIR</div>
  <div class="abs" style="left:41px;top:59px;width:24px;height:24px;border-radius:50%;background:var(--tan);color:#fff;font:700 11px/24px Poppins,sans-serif;text-align:center">1</div>
  <div class="abs" style="left:73px;top:60px;width:90px">
    <div style="font:600 13px/1.1 Poppins,sans-serif;color:var(--navy)">Lorem<br>ipsum dolor<br>sit amet</div>
    <p style="margin:5px 0 0;font:400 5.3px/1.35 Poppins,sans-serif;color:var(--grey)">Praesent bibendum at risus ac blandit. In eu risus vel felis elementum venenatis vitae sed lacus. Curabitur vel erat urna.</p>
  </div>
  <div class="abs" style="left:184px;top:51px;width:118px;height:104px;background:var(--navy)"></div>
  <div class="abs" style="left:172px;top:57px;width:24px;height:24px;border-radius:50%;background:var(--tan);color:#fff;font:700 11px/24px Poppins,sans-serif;text-align:center">2</div>
  <div class="abs" style="left:203px;top:58px;width:92px">
    <div style="font:600 13px/1.1 Poppins,sans-serif;color:#fff">Lorem<br>ipsum dolor<br>sit amet</div>
    <p style="margin:5px 0 0;font:400 5.3px/1.35 Poppins,sans-serif;color:#fff">Praesent bibendum at risus ac blandit. In eu risus vel felis elementum venenatis vitae sed lacus. Curabitur vel erat urna.</p>
  </div>
  <div class="peak" role="img" aria-label="Mountain ridge decoration"></div>
  <div class="base"></div><div class="pg">08</div>
</section>

<section class="slide c3 r3">
  <div class="abs" style="left:0;top:0;width:128px;height:201px;background:var(--navy)"></div>
  <h2 class="title light">Text Here</h2>
  <div class="brand">ALTAVIR</div>
  <div class="abs" style="left:11px;top:38px;width:108px">
    <p class="tiny light" style="font-size:3.9px">Lorem ipsum dolor sit amet, consectetuer adipiscing elit, sed diam nonummy nibh euismod tincidunt ut laoreet dolore magna aliquam erat volutpat. Ut wisi enim ad minim veniam, quis nostrud exerci tation ullamcorper suscipit lobortis nisl ut aliquip ex ea commodo consequat. Duis autem vel eum iriure dolor in hendrerit i</p>
    <p class="tiny light" style="font-size:3.9px;margin-top:5px">Lorem ipsum dolor sit amet, consectetuer adipiscing elit, sed diam nonummy nibh . Lorem ipsum dolor sit amet, consec-tetuer adipiscing elit, sed diam nonummy nibh euismod tincidunt ut laoreet dolore magna aliquam erat volutpat. Ut wisi</p>
  </div>
  <div class="abs" style="left:150px;top:25px;font:500 6px/1 Poppins,sans-serif;color:var(--navy)">CONSECTETUER ADIPISCING</div>
  <svg class="abs" style="left:0;top:0" width="358" height="201" viewBox="0 0 358 201" role="img" aria-label="Bar chart, January to April">
    <g stroke="#d5d5d5" stroke-width=".5">
      <line x1="156" y1="41" x2="323" y2="41"/><line x1="156" y1="54" x2="323" y2="54"/><line x1="156" y1="67" x2="323" y2="67"/>
      <line x1="156" y1="80" x2="323" y2="80"/><line x1="156" y1="93" x2="323" y2="93"/><line x1="156" y1="106" x2="323" y2="106"/>
      <line x1="156" y1="119" x2="323" y2="119"/><line x1="156" y1="41" x2="156" y2="119"/><line x1="323" y1="41" x2="323" y2="119"/>
    </g>
    <g font-size="5.5" fill="#333" text-anchor="end">
      <text x="153" y="43">60</text><text x="153" y="56">50</text><text x="153" y="69">40</text><text x="153" y="82">30</text>
      <text x="153" y="95">20</text><text x="153" y="108">10</text><text x="153" y="121">0</text>
    </g>
    <rect x="170" y="47.5" width="19" height="71.5" fill="var(--navy)"/>
    <rect x="206" y="77.4" width="19" height="41.6" fill="var(--tan)"/>
    <rect x="242" y="57.9" width="19" height="61.1" fill="var(--navy)"/>
    <rect x="278" y="82.6" width="19" height="36.4" fill="var(--sand)"/>
    <g font-size="5.5" fill="#333" text-anchor="middle">
      <text x="179.5" y="129">JAN</text><text x="215.5" y="129">FEB</text><text x="251.5" y="129">MAR</text><text x="287.5" y="129">APR</text>
    </g>
  </svg>
  <div class="abs" style="left:147px;top:143px;width:90px"><div style="font:500 6px/1 Poppins,sans-serif;color:var(--navy)"><span class="legend-dot" style="background:var(--tan)"></span>Lorem ipsum</div><p class="tiny" style="margin:2px 0 0 8px">Lorem ipsum dolor sit amet, consectetuer adipiscing elit, sed diam nonummy nibh euismod tincidunt ut laoreet</p></div>
  <div class="abs" style="left:244px;top:143px;width:90px"><div style="font:500 6px/1 Poppins,sans-serif;color:var(--navy)"><span class="legend-dot" style="background:var(--tan)"></span>Lorem ipsum</div><p class="tiny" style="margin:2px 0 0 8px">Lorem ipsum dolor sit amet, consectetuer adipiscing elit, sed diam nonummy nibh euismod tincidunt ut laoreet</p></div>
  <div class="peak" role="img" aria-label="Mountain ridge decoration"></div>
  <div class="base"></div><div class="pg">09</div>
</section>

<section class="slide c1 r4">
  <h2 class="title">Text Here</h2>
  <div class="brand">ALTAVIR</div>
  <div class="abs" style="left:12px;top:35px;width:143px">
    <p class="tiny">Lorem ipsum dolor sit amet, consectetuer adipiscing elit, sed diam nonummy nibh euismod tincidunt ut laoreet dolore magna aliquam erat volutpat. Ut wisi enim ad minim veniam, quis nostrud exerci tation ullamcorper suscipit lobortis nisl ut aliquip ex ea commodo consequat. Duis autem vel eum iriure dolor in hendrerit i</p>
    <p class="tiny" style="margin-top:4px">m ipsum dolor sit amet, consectetuer adipiscing elit, sed diam nonummy nibh euismod tincidunt ut laoreet dolore magna aliquam erat volutpat. Ut wisi enim ad minim veniam, quis nostrud exerci tation ullamcorper suscipit lobortis nisl ut aliquip ex ea commodo</p>
  </div>
  <svg class="abs" style="left:0;top:0" width="358" height="201" viewBox="0 0 358 201" role="img" aria-label="Bar chart and line chart">
    <g stroke="#dcdcdc" stroke-width=".4">
      <line x1="14" y1="99" x2="151" y2="99"/><line x1="14" y1="109" x2="151" y2="109"/><line x1="14" y1="119" x2="151" y2="119"/>
      <line x1="14" y1="129" x2="151" y2="129"/><line x1="14" y1="140" x2="151" y2="140"/><line x1="14" y1="150" x2="151" y2="150"/>
      <line x1="14" y1="160" x2="151" y2="160"/>
    </g>
    <g font-size="4.5" fill="#333" text-anchor="end">
      <text x="11" y="101">60</text><text x="11" y="111">50</text><text x="11" y="121">40</text><text x="11" y="131">30</text>
      <text x="11" y="142">20</text><text x="11" y="152">10</text><text x="11" y="162">0</text>
    </g>
    <rect x="32" y="119" width="4" height="41" fill="var(--navy)"/><rect x="38" y="109" width="4" height="51" fill="var(--tan)"/>
    <rect x="61" y="149" width="4" height="11" fill="var(--tan)"/><rect x="67" y="124" width="4" height="36" fill="var(--navy)"/>
    <rect x="89" y="102" width="4" height="58" fill="var(--tan)"/><rect x="95" y="147" width="4" height="13" fill="var(--navy)"/>
    <rect x="117" y="108" width="4" height="52" fill="var(--navy)"/><rect x="123" y="130" width="4" height="30" fill="var(--tan)"/>
    <g font-size="4.5" fill="#333" text-anchor="middle">
      <text x="39" y="168">JAN</text><text x="67" y="168">FEB</text><text x="96" y="168">MAR</text><text x="124" y="168">APR</text>
    </g>
    <g stroke="#dcdcdc" stroke-width=".4">
      <line x1="184" y1="39" x2="323" y2="39"/><line x1="184" y1="48" x2="323" y2="48"/><line x1="184" y1="56" x2="323" y2="56"/>
      <line x1="184" y1="65" x2="323" y2="65"/><line x1="184" y1="74" x2="323" y2="74"/><line x1="184" y1="82" x2="323" y2="82"/>
      <line x1="184" y1="91" x2="323" y2="91"/><line x1="323" y1="39" x2="323" y2="91"/>
    </g>
    <g font-size="3.8" fill="#333" text-anchor="end">
      <text x="181" y="41">60</text><text x="181" y="50">50</text><text x="181" y="58">40</text><text x="181" y="67">30</text>
      <text x="181" y="76">20</text><text x="181" y="84">10</text><text x="181" y="93">0</text>
    </g>
    <polyline fill="none" stroke="var(--navy)" stroke-width=".8" points="187,91 202,82 217,65 232,75 247,56 262,68 277,69 292,74 307,65 322,56"/>
    <polyline fill="none" stroke="var(--tan)" stroke-width=".8" points="187,89 202,87 217,72 232,49 247,56 262,63 277,69 292,60 307,56 322,82"/>
    <g fill="var(--navy)"><circle cx="187" cy="91" r="1"/><circle cx="202" cy="82" r="1"/><circle cx="217" cy="65" r="1"/><circle cx="232" cy="75" r="1"/><circle cx="247" cy="56" r="1"/><circle cx="262" cy="68" r="1"/><circle cx="277" cy="69" r="1"/><circle cx="292" cy="74" r="1"/><circle cx="307" cy="65" r="1"/><circle cx="322" cy="56" r="1"/></g>
    <g font-size="2.6" fill="#555" text-anchor="middle">
      <text x="192" y="97">TEXT 01</text><text x="207" y="97">TEXT 02</text><text x="222" y="97">TEXT 03</text><text x="237" y="97">TEXT 04</text><text x="252" y="97">TEXT 05</text>
      <text x="267" y="97">TEXT 06</text><text x="282" y="97">TEXT 07</text><text x="297" y="97">TEXT 08</text><text x="312" y="97">TEXT 09</text>
    </g>
  </svg>
  <div class="abs" style="left:175px;top:120px;width:80px"><div style="font:500 5.5px/1 Poppins,sans-serif;color:var(--navy)"><span class="legend-dot" style="background:var(--tan);width:4px;height:4px"></span>Lorem ipsum</div><p class="tiny" style="margin:2px 0 0 10px;font-size:3px">Lorem ipsum dolor sit amet, consectetuer adipiscing elit, sed diam nonummy nibh euismod</p></div>
  <div class="abs" style="left:261px;top:120px;width:80px"><div style="font:500 5.5px/1 Poppins,sans-serif;color:var(--tan)"><span class="legend-dot" style="background:var(--navy);width:4px;height:4px"></span>Lorem ipsum</div><p class="tiny" style="margin:2px 0 0 10px;font-size:3px">Lorem ipsum dolor sit amet, consectetuer adipiscing elit, sed diam nonummy nibh euismod</p></div>
  <div class="abs" style="left:175px;top:146px;width:80px"><div style="font:500 5.5px/1 Poppins,sans-serif;color:var(--tan)"><span class="legend-dot" style="background:var(--navy);width:4px;height:4px"></span>Lorem ipsum</div><p class="tiny" style="margin:2px 0 0 10px;font-size:3px">Lorem ipsum dolor sit amet, consectetuer adipiscing elit, sed diam nonummy nibh euismod</p></div>
  <div class="abs" style="left:261px;top:146px;width:80px"><div style="font:500 5.5px/1 Poppins,sans-serif;color:var(--navy)"><span class="legend-dot" style="background:var(--tan);width:4px;height:4px"></span>Lorem ipsum</div><p class="tiny" style="margin:2px 0 0 10px;font-size:3px">Lorem ipsum dolor sit amet, consectetuer adipiscing elit, sed diam nonummy nibh euismod</p></div>
  <div class="peak" role="img" aria-label="Mountain ridge decoration"></div>
  <div class="base"></div><div class="pg">10</div>
</section>

<section class="slide c2 r4">
  <div class="abs" style="left:0;top:0;width:358px;height:74px;background:var(--navy)"></div>
  <h2 class="title light">Text Here</h2>
  <div class="brand on-dark">ALTAVIR</div>
  <div class="photo mono" style="left:26px;top:38px;width:296px;height:88px" role="img" aria-label="Black and white photo of soldiers crawling through sand"></div>
  <div class="tab" style="left:40px;top:115px">01</div>
  <div class="tab" style="left:145px;top:115px">02</div>
  <div class="tab" style="left:250px;top:115px">03</div>
  <p class="tiny abs" style="left:38px;top:131px;width:70px">Lorem ipsum Dolor sit amet Consectetur adipiscing<br><br>sed do eiusmod Tempor incididunt ut labore et dolore</p>
  <p class="tiny abs" style="left:143px;top:131px;width:70px">Lorem ipsum Dolor sit amet Consectetur adipiscing<br><br>sed do eiusmod Tempor incididunt ut labore et dolore</p>
  <p class="tiny abs" style="left:248px;top:131px;width:70px">Lorem ipsum Dolor sit amet Consectetur adipiscing<br><br>sed do eiusmod Tempor incididunt ut labore et dolore</p>
  <div class="peak" role="img" aria-label="Mountain ridge decoration"></div>
  <div class="base"></div><div class="pg">11</div>
</section>

<section class="slide c3 r4">
  <h2 class="title">Text Here</h2>
  <div class="brand">ALTAVIR</div>
  <svg class="abs" style="left:0;top:0" width="358" height="201" viewBox="0 0 358 201" role="img" aria-label="Stacked percentage bars for 2019 to 2021">
    <line x1="72" y1="37" x2="72" y2="127" stroke="var(--navy)" stroke-width=".8"/>
    <circle cx="72" cy="38" r="1.5" fill="var(--navy)"/>
    <line x1="72" y1="127" x2="300" y2="127" stroke="var(--navy)" stroke-width=".8"/>
    <g fill="var(--navy)">
      <circle cx="72" cy="127" r="1.4"/><circle cx="95" cy="127" r="1.4"/><circle cx="118" cy="127" r="1.4"/><circle cx="140" cy="127" r="1.4"/><circle cx="163" cy="127" r="1.4"/><circle cx="186" cy="127" r="1.4"/><circle cx="209" cy="127" r="1.4"/><circle cx="232" cy="127" r="1.4"/><circle cx="254" cy="127" r="1.4"/><circle cx="277" cy="127" r="1.4"/><circle cx="300" cy="127" r="1.4"/>
    </g>
    <g font-size="5.5" fill="var(--tan)" text-anchor="middle">
      <text x="72" y="137">0%</text><text x="95" y="137">10%</text><text x="118" y="137">20%</text><text x="140" y="137">30%</text><text x="163" y="137">40%</text><text x="186" y="137">50%</text><text x="209" y="137">60%</text><text x="232" y="137">70%</text><text x="254" y="137">80%</text><text x="277" y="137">90%</text><text x="300" y="137">100%</text>
    </g>
    <g font-size="6.5" font-weight="500" fill="var(--tan)">
      <text x="52" y="59">2019</text><text x="52" y="86">2020</text><text x="52" y="112">2021</text>
    </g>
    <g fill="var(--navy)"><circle cx="43" cy="57" r="2.6"/><circle cx="43" cy="84" r="2.6"/><circle cx="43" cy="110" r="2.6"/></g>
    <rect x="72" y="47" width="33" height="18" fill="var(--tan)"/><rect x="105" y="47" width="45" height="18" fill="var(--sand)"/><rect x="150" y="47" width="32" height="18" fill="var(--navy)"/><rect x="182" y="47" width="115" height="18" fill="var(--tan)"/>
    <rect x="72" y="74" width="80" height="18" fill="var(--navy)"/><rect x="152" y="74" width="56" height="18" fill="var(--sand)"/><rect x="208" y="74" width="45" height="18" fill="var(--tan)"/><rect x="253" y="74" width="44" height="18" fill="var(--tan)"/>
    <rect x="72" y="101" width="46" height="18" fill="var(--tan)"/><rect x="118" y="101" width="67" height="18" fill="var(--sand)"/><rect x="185" y="101" width="24" height="18" fill="var(--navy)"/><rect x="209" y="101" width="88" height="18" fill="var(--sand)"/>
    <g font-size="5.5" text-anchor="middle">
      <text x="88" y="58" fill="#fff">20%</text><text x="127" y="58" fill="var(--navy)">40%</text><text x="166" y="58" fill="#fff">10%</text><text x="240" y="58" fill="#fff">90%</text>
      <text x="112" y="85" fill="#fff">50%</text><text x="180" y="85" fill="var(--navy)">30%</text><text x="230" y="85" fill="#fff">20%</text><text x="275" y="85" fill="#fff">20%</text>
      <text x="95" y="112" fill="#fff">30%</text><text x="151" y="112" fill="var(--navy)">60%</text><text x="197" y="112" fill="#fff">10%</text><text x="253" y="112" fill="var(--navy)">70%</text>
    </g>
  </svg>
  <div class="abs" style="left:68px;top:146px;width:58px"><div style="font:500 5.5px/1 Poppins,sans-serif;color:var(--tan)">Lorem Ipsum</div><p class="tiny" style="font-size:3px;margin-top:1px">Lorem ipsum dolor sit amet, adipiscing elit, sed diam nonummy nibh euismod</p></div>
  <div class="abs" style="left:130px;top:146px;width:58px"><div style="font:500 5.5px/1 Poppins,sans-serif;color:var(--navy)">Lorem Ipsum</div><p class="tiny" style="font-size:3px;margin-top:1px">Lorem ipsum dolor sit amet, consectetuer adipiscing e</p></div>
  <div class="abs" style="left:193px;top:146px;width:58px"><div style="font:500 5.5px/1 Poppins,sans-serif;color:var(--tan)">Lorem Ipsum</div><p class="tiny" style="font-size:3px;margin-top:1px">Lorem ipsum dolor sit amet, consectetuer adipiscing elit, sed diam nonummy nibh</p></div>
  <div class="abs" style="left:258px;top:146px;width:58px"><div style="font:500 5.5px/1 Poppins,sans-serif;color:var(--navy)">Lorem Ipsum</div><p class="tiny" style="font-size:3px;margin-top:1px">Lorem ipsum dolor sit amet, adipiscing elit, sed diam nonummy</p></div>
  <div class="peak" role="img" aria-label="Mountain ridge decoration"></div>
  <div class="base"></div><div class="pg">12</div>
</section>

<section class="slide c1 r5">
  <div class="abs" style="left:0;top:0;width:124px;height:201px;background:var(--navy)"></div>
  <h2 class="title light">Text Here</h2>
  <div class="brand">ALTAVIR</div>
  <div class="abs" style="left:11px;top:38px;width:106px">
    <p class="tiny light" style="font-size:4.6px;line-height:1.3">Lorem ipsum dolor sit amet, consectetuer adipiscing elit, sed diam nonummy nibh euismod tincidunt ut laoreet dolore magna aliquam erat volutpat. Ut wisi enim ad minim veniam,</p>
    <p class="tiny light" style="font-size:4.6px;line-height:1.3;margin-top:5px">quis nostrud exerci tation ullamcorper suscipit lobortis nisl ut aliquip ex ea commodo consequat. Duis autem vel eum iriure dolor in hendrerit in vulputate velit esse</p>
  </div>
  <div class="abs" style="left:17px;top:117px;width:100px">
    <div style="display:flex;gap:4px;margin-bottom:8px"><span style="background:var(--sand);color:var(--navy);font:700 7px/9px Poppins,sans-serif;width:10px;text-align:center">1.</span><div><div style="font:500 4.8px/1 Poppins,sans-serif;color:#fff">Lorem ipsum</div><p class="tiny light" style="font-size:2.8px">Lorem ipsum dolor sit amet, consectetuer<br>adipiscing elit, sed diam nonummy nibh</p></div></div>
    <div style="display:flex;gap:4px;margin-bottom:8px"><span style="background:var(--sand);color:var(--navy);font:700 7px/9px Poppins,sans-serif;width:10px;text-align:center">2.</span><div><div style="font:500 4.8px/1 Poppins,sans-serif;color:#fff">Lorem ipsum</div><p class="tiny light" style="font-size:2.8px">Lorem ipsum dolor sit amet, consectetuer<br>adipiscing elit, sed diam nonummy nibh</p></div></div>
    <div style="display:flex;gap:4px"><span style="background:var(--sand);color:var(--navy);font:700 7px/9px Poppins,sans-serif;width:10px;text-align:center">3.</span><div><div style="font:500 4.8px/1 Poppins,sans-serif;color:#fff">Lorem ipsum</div><p class="tiny light" style="font-size:2.8px">Lorem ipsum dolor sit amet, consectetuer<br>adipiscing elit, sed diam nonummy nibh</p></div></div>
  </div>
  <div class="phone" style="left:150px;top:19px">Lorem<br>ipsum dolor<p class="tiny" style="font-size:2.4px;margin-top:18px">To introduce the students to the changing landscape of marketing and equip them with knowledge and tools to navigate the digital marketing world.</p></div>
  <div class="phone" style="left:204px;top:46px">Dolor sit<br>amet, conse<p class="tiny" style="font-size:2.4px;margin-top:18px">You will learn concepts and ideas in digital marketing as well as how to use different tools and strategies to optimise your digital marketing campaigns.</p></div>
  <div class="phone" style="left:259px;top:77px">Consec<p class="tiny" style="font-size:2.4px;margin-top:22px">You are required to pass 80% of the evaluation test to obtain the certificate. The evaluation test can only be taken 3 times.</p></div>
  <div class="peak" role="img" aria-label="Mountain ridge decoration"></div>
  <div class="base"></div><div class="pg">13</div>
</section>

<section class="slide c2 r5">
  <h2 class="title">Text Here</h2>
  <div class="brand">ALTAVIR</div>
  <div class="abs" style="left:12px;top:33px;width:322px">
    <p class="tiny" style="font-size:4.2px">Lorem ipsum dolor sit amet, consectetuer adipiscing elit, sed diam nonummy nibh euismod tincidunt ut laoreet dolore magna aliquam erat volutpat. Ut wisi enim ad minim veniam, quis nostrud exerci tation ullamcorper suscipit lobortis nisl ut aliquip ex ea commodo consequat. Duis autem vel eum iriure dolor in hendrerit in vulputate velit esse molestie consequat, vel illum dolore eu feugiat nulla facilisis at vero eros et accumsan et iusto odio dignissim qui blandit praesent luptatum zzril delenit augue duis dolore te feugait nulla facilisi.</p>
    <p class="tiny" style="font-size:4.2px;margin-top:4px">Lorem ipsum dolor sit amet, cons ectetuer adipiscing elit, sed diam nonummy nibh euismod tincidunt ut laoreet dolore magna aliquam erat volutpat. Ut wisi enim ad minim veniam, quis nostrud exerci tation ullamcorper suscipit lobortis nisl ut aliquip ex</p>
  </div>
  <div class="abs" style="left:0;top:102px;width:358px;height:59px;background:var(--navy)"></div>
  <div class="person" style="left:36px;top:86px" role="img" aria-label="Team member portrait"></div>
  <div class="person" style="left:123px;top:86px" role="img" aria-label="Team member portrait"></div>
  <div class="person" style="left:207px;top:86px" role="img" aria-label="Team member portrait"></div>
  <div class="person" style="left:293px;top:86px" role="img" aria-label="Team member portrait"></div>
  <div class="person-name" style="left:13px;top:124px">ALEX REED</div>
  <div class="person-name" style="left:100px;top:124px">NORA HALE</div>
  <div class="person-name" style="left:184px;top:124px">ALEX REED</div>
  <div class="person-name" style="left:270px;top:124px">NORA HALE</div>
  <p class="tiny light abs" style="left:22px;top:131px;width:52px;text-align:center;font-size:2.8px">ipsum dolor sit amet, cons ectetuer adipiscing elit, sed diam nonummy nibh euismod tincidunt ut laoreet dolore magna aliquam erat volutpat.</p>
  <p class="tiny light abs" style="left:109px;top:131px;width:52px;text-align:center;font-size:2.8px">ipsum dolor sit amet, cons ectetuer adipiscing elit, sed diam nonummy nibh euismod tincidunt ut laoreet dolore magna aliquam erat volutpat.</p>
  <p class="tiny light abs" style="left:193px;top:131px;width:52px;text-align:center;font-size:2.8px">ipsum dolor sit amet, cons ectetuer adipiscing elit, sed diam nonummy nibh euismod tincidunt ut laoreet dolore magna aliquam erat volutpat.</p>
  <p class="tiny light abs" style="left:279px;top:131px;width:52px;text-align:center;font-size:2.8px">ipsum dolor sit amet, cons ectetuer adipiscing elit, sed diam nonummy nibh euismod tincidunt ut laoreet dolore magna aliquam erat volutpat.</p>
  <div class="peak" role="img" aria-label="Mountain ridge decoration"></div>
  <div class="base"></div><div class="pg">14</div>
</section>

<section class="slide c3 r5">
  <div class="abs" style="left:0;top:0;width:358px;height:92px;background:var(--navy)"></div>
  <div class="abs" style="left:0;right:0;top:26px;text-align:center;font:600 14px/1 Poppins,sans-serif;color:#fff">Thank You</div>
  <div class="abs" style="left:0;right:0;top:80px;text-align:center;font:700 24px/1 'Roboto Condensed',sans-serif;letter-spacing:3px;color:var(--tan)">ALTAVIR</div>
  <div class="abs" style="left:81px;top:163px;font:400 13px/1 Poppins,sans-serif;letter-spacing:.5px;color:var(--navy)">CONTACT US</div>
  <svg class="abs" style="left:182px;top:160px" width="8" height="22" viewBox="0 0 8 22" aria-hidden="true">
    <circle cx="4" cy="4" r="3.5" fill="var(--navy)"/><path d="M2.6 2.4 q.3 2.6 2.8 3.2 l.6-.8" stroke="#fff" stroke-width=".7" fill="none"/>
    <circle cx="4" cy="17" r="3.5" fill="var(--navy)"/><rect x="2.2" y="15.7" width="3.6" height="2.6" fill="none" stroke="#fff" stroke-width=".5"/>
  </svg>
  <div class="abs" style="left:192px;top:160px;font:400 6.8px/13px Poppins,sans-serif;color:var(--navy)">0400 123 456<br>hello@altavir.example</div>
</section>

</body>
</html>
```